Menu Design Project for new restauranct concept

Design menu for new restaurant concept called Juniper's Burgers & Dogs. Logo is attached.

Industry/Entity Type

Restaurant

Requirements
Must have
• Menu items and pricing:

Burgers
Snack Burger $3.49
Snack Cheeseburger $3.99
Juniper's signature Burger $4.99
Juniper's signature Cheeseburger $5.49
Burger toppings: bacon, lettuce, tomato, onion, pickle, grilled onions, grilled mushrooms, grilled green peppers, jalapeƱo peppers.

Dogs
Hot Dog $2.99
Bacon Cheese Hot Dog $3.99
Slaw Dog $3.99
Kraut Dog $3.49
Chili Dog $3.99 with or with out cheese
Hot dogs are 100% beef

Other
Grilled Chicken Sandwich $5.99
Grilled Chicken Sandwich with cheese $6.49
(Same toppings as burgers)

French Fries $1.99

Loaded Potatos
The Plain Tater: $4.99 choose from: butter, sour cream, cheese, chives
The Garden Tater: $5.99 choose from: the Basic plus, broccoli & cheese, grilled mushrooms, onions, & peppers
The Carver Tater: $6.99 choose from the Basic/Veggie plus: grilled chicken, chili, Philly cheesesteak, pulled pork.

Drinks
32oz. Drink $1.88
20oz. Drink $1.69

attached logo.
Nice to have
• love to incorporate the woodgrain backgound. It makes the logo look most like a cattle brand, which we like.

```html
<!DOCTYPE html>
<html lang="en">
<head>
<meta charset="utf-8">
<title>Juniper's Burgers &amp; Dogs — Menu</title>
<link rel="stylesheet" href="https://fonts.googleapis.com/css2?family=Oswald:wght@400;500;700&display=swap">
<style>
  :root {
    --wood-dark: #3a2414;
    --wood-mid: #5a3a22;
    --wood-light: #7a5436;
    --divider: #ece6de;
    --card: #ffffff;
    --ink: #111111;
    --on-wood: #ffffff;
  }
  * { margin: 0; padding: 0; box-sizing: border-box; }
  html, body { width: 927px; height: 1200px; overflow: hidden; background: var(--divider); }
  .sheet { position: relative; width: 927px; height: 1200px; }
  .panel { position: absolute; top: 0; width: 460px; height: 1200px; overflow: hidden; }
  .panel--left { left: 0; }
  .panel--right { left: 467px; }
  .wood {
    position: absolute; inset: 0;
    background: linear-gradient(100deg, var(--wood-mid) 0%, var(--wood-dark) 30%, var(--wood-light) 55%, var(--wood-mid) 75%, var(--wood-dark) 100%);
  }
  .brand {
    position: absolute; left: 0; right: 0; top: 70px;
    text-align: center; color: var(--on-wood);
    font-family: "Oswald", sans-serif; font-weight: 700; text-transform: uppercase;
    line-height: 1.05;
  }
  .brand__name { display: block; font-size: 46px; letter-spacing: 1px; }
  .brand__tag { display: block; font-size: 19px; letter-spacing: 0.5px; margin-top: 16px; }
  .card {
    position: absolute; left: 45px; top: 238px; width: 373px; height: 853px;
    background: var(--card); color: var(--ink);
    font-family: "Oswald", sans-serif; text-transform: uppercase;
  }
  .line {
    position: absolute; left: 0; right: 0; text-align: center;
    transform: translateY(-50%); white-space: nowrap;
    font-size: 13.5px; font-weight: 400; line-height: 1;
  }
  .line b { font-weight: 700; }
  .heading { font-size: 26px; font-weight: 700; letter-spacing: 0.3px; }
  .note { font-size: 11px; letter-spacing: -0.2px; }
  .bold { font-weight: 700; }
  .badge { position: absolute; left: 255px; top: 196px; width: 50px; height: 50px; }
  .footer {
    position: absolute; left: 0; right: 0; top: 1103px;
    text-align: center; color: var(--on-wood);
    font-family: "Oswald", sans-serif; font-weight: 700; font-size: 12.5px;
    text-transform: uppercase; line-height: 19px;
  }
</style>
</head>
<body>
<main class="sheet">

  <section class="panel panel--left">
    <div class="wood" role="img" aria-label="Dark brown woodgrain planks background"></div>
    <h1 class="brand"><span class="brand__name">Juniper's</span><span class="brand__tag">Burgers &amp; Dogs</span></h1>
    <div class="card">
      <h2 class="line heading" style="top:37px">Burgers</h2>
      <p class="line" style="top:70px">Snack Burger <b>$3.49</b></p>
      <p class="line" style="top:91px">Snack Cheeseburger <b>$3.99</b></p>
      <p class="line" style="top:115px">Juniper's Signature Burger <b>$4.99</b></p>
      <p class="line" style="top:139px">Juniper's Signature Cheeseburger <b>$5.49</b></p>
      <p class="line note" style="top:159px">Toppings: bacon, lettuce, tomato, onion, pickle, grilled onions,</p>
      <p class="line note" style="top:177px">grilled mushrooms, grilled green peppers, jalapeño peppers</p>

      <h2 class="line heading" style="top:221px">Dogs</h2>
      <svg class="badge" viewBox="0 0 50 50" aria-hidden="true"><circle cx="25" cy="25" r="23" fill="#fff" stroke="#111" stroke-width="2.5"/><circle cx="25" cy="25" r="18.5" fill="none" stroke="#111" stroke-width="1.5"/></svg>
      <p class="line" style="top:253px">Hot Dog <b>$2.99</b></p>
      <p class="line" style="top:275px">Bacon Cheese Hot Dog <b>$3.99</b></p>
      <p class="line" style="top:296px">Slaw Dog <b>$3.99</b></p>
      <p class="line" style="top:318px">Kraut Dog <b>$3.49</b></p>
      <p class="line" style="top:340px">Chili Dog <b>$3.99</b></p>
      <p class="line note" style="top:361px">With or with out cheese</p>

      <h2 class="line heading" style="top:405px">Other</h2>
      <p class="line" style="top:438px">Grilled Chicken Sandwich <b>$5.99</b></p>
      <p class="line" style="top:460px">Grilled Chicken Sandwich with Cheese <b>$6.49</b></p>
      <p class="line note" style="top:481px">(Same toppings as burgers)</p>
      <p class="line bold" style="top:510px">French Fries $1.99</p>

      <h2 class="line heading" style="top:554px">Loaded Potatoes</h2>
      <p class="line" style="top:585px">The Plain Tater: <b>$4.99</b></p>
      <p class="line note" style="top:604px">Choose: butter, sour cream, cheese, chives</p>
      <p class="line" style="top:625px">The Garden Tater: <b>$5.99</b></p>
      <p class="line note" style="top:644px">Choose: the basic plus, broccoli &amp; cheese,</p>
      <p class="line note" style="top:663px">grilled mushrooms, onions, &amp; peppers</p>
      <p class="line" style="top:684px">The Carver Tater: <b>$6.99</b></p>
      <p class="line note" style="top:704px">Choose basic/veggie plus: grilled chicken, chili,</p>
      <p class="line note" style="top:723px">Philly cheesesteak, pulled pork</p>

      <h2 class="line heading" style="top:767px">Drinks</h2>
      <p class="line" style="top:799px">32oz. Drink <b>$1.88</b></p>
      <p class="line" style="top:819px">20oz. Drink <b>$1.69</b></p>
    </div>
    <address class="footer">junipersburgers.com<br>214 Cedar Ave USA 10047<br>555.214.0190</address>
  </section>

  <section class="panel panel--right">
    <div class="wood" role="img" aria-label="Dark brown woodgrain planks background"></div>
    <h1 class="brand"><span class="brand__name">Juniper's</span><span class="brand__tag">Burgers &amp; Dogs</span></h1>
    <div class="card">
      <h2 class="line heading" style="top:37px">Burgers</h2>
      <p class="line" style="top:70px">Snack Burger <b>$3.49</b></p>
      <p class="line" style="top:91px">Snack Cheeseburger <b>$3.99</b></p>
      <p class="line" style="top:115px">Juniper's Signature Burger <b>$4.99</b></p>
      <p class="line" style="top:139px">Juniper's Signature Cheeseburger <b>$5.49</b></p>
      <p class="line note" style="top:159px">Toppings: bacon, lettuce, tomato, onion, pickle, grilled onions,</p>
      <p class="line note" style="top:177px">grilled mushrooms, grilled green peppers, jalapeño peppers</p>

      <h2 class="line heading" style="top:221px">Dogs</h2>
      <svg class="badge" viewBox="0 0 50 50" aria-hidden="true"><circle cx="25" cy="25" r="23" fill="#fff" stroke="#111" stroke-width="2.5"/><circle cx="25" cy="25" r="18.5" fill="none" stroke="#111" stroke-width="1.5"/></svg>
      <p class="line" style="top:253px">Hot Dog <b>$2.99</b></p>
      <p class="line" style="top:275px">Bacon Cheese Hot Dog <b>$3.99</b></p>
      <p class="line" style="top:296px">Slaw Dog <b>$3.99</b></p>
      <p class="line" style="top:318px">Kraut Dog <b>$3.49</b></p>
      <p class="line" style="top:340px">Chili Dog <b>$3.99</b></p>
      <p class="line note" style="top:361px">With or with out cheese</p>

      <h2 class="line heading" style="top:405px">Other</h2>
      <p class="line" style="top:438px">Grilled Chicken Sandwich <b>$5.99</b></p>
      <p class="line" style="top:460px">Grilled Chicken Sandwich with Cheese <b>$6.49</b></p>
      <p class="line note" style="top:481px">(Same toppings as burgers)</p>
      <p class="line bold" style="top:510px">French Fries $1.99</p>

      <h2 class="line heading" style="top:554px">Loaded Potatoes</h2>
      <p class="line" style="top:585px">The Plain Tater: <b>$4.99</b></p>
      <p class="line note" style="top:604px">Choose: butter, sour cream, cheese, chives</p>
      <p class="line" style="top:625px">The Garden Tater: <b>$5.99</b></p>
      <p class="line note" style="top:644px">Choose: the basic plus, broccoli &amp; cheese,</p>
      <p class="line note" style="top:663px">grilled mushrooms, onions, &amp; peppers</p>
      <p class="line" style="top:684px">The Carver Tater: <b>$6.99</b></p>
      <p class="line note" style="top:704px">Choose basic/veggie plus: grilled chicken, chili,</p>
      <p class="line note" style="top:723px">Philly cheesesteak, pulled pork</p>

      <h2 class="line heading" style="top:767px">Drinks</h2>
      <p class="line" style="top:799px">32oz. Drink <b>$1.88</b></p>
      <p class="line" style="top:819px">20oz. Drink <b>$1.69</b></p>
    </div>
    <address class="footer">junipersburgers.com<br>214 Cedar Ave USA 10047<br>555.214.0190</address>
  </section>

</main>
</body>
</html>
```